ZRT Pty Ltd business card

we need to get a business card designed. We're a large whole seller of baby formula , health supplement and cosmetic products.

Target Market(s)

Big online E commerce platforms, supermarket channels in Asia.

Industry/Entity Type

Business

Contact Information for Business Card

glossy

Logo Text

ZRT

Colors
abd036

Requirements
Must have
• ZRT

```html
<!DOCTYPE html>
<html lang="en">
<head>
<meta charset="utf-8">
<title>ZRT Pty Ltd business card</title>
<link rel="stylesheet" href="https://fonts.googleapis.com/css2?family=Roboto+Slab:wght@300;400;600;700&display=swap">
<style>
  :root {
    --backdrop: #222222;
    --card: #ffffff;
    --ink: #33403f;
    --brand-green: #abd036;
    --photo-light: #f3d2bd;
    --photo-mid: #e2b190;
  }
  html, body {
    margin: 0;
    padding: 0;
    width: 1200px;
    height: 1076px;
    overflow: hidden;
    background: var(--backdrop);
  }
  .sheet {
    width: 1200px;
    height: 1076px;
    display: flex;
    flex-direction: column;
    align-items: center;
    justify-content: center;
    gap: 30px;
  }
  .card {
    display: block;
    width: 840px;
    height: 485px;
    font-family: "Roboto Slab", Georgia, serif;
  }
  .card-face { fill: var(--card); }
  .brand-dot { fill: var(--brand-green); }
  .brand-name { fill: var(--ink); font-weight: 600; font-size: 118px; }
  .brand-suffix { fill: var(--ink); font-weight: 400; font-size: 34px; }
  .web-address { font-size: 24px; font-weight: 400; fill: var(--ink); }
  .web-address .accent { fill: var(--brand-green); }
  .person-name { fill: var(--ink); font-weight: 700; font-size: 36px; }
  .person-role { fill: var(--brand-green); font-weight: 300; font-size: 25px; }
  .contact-line { fill: var(--ink); font-weight: 300; font-size: 25px; }
  .contact-label { fill: var(--brand-green); font-weight: 600; }
</style>
</head>
<body>
<main class="sheet">

  <!-- Back of card -->
  <svg class="card card-back" viewBox="0 0 910 525" xmlns="http://www.w3.org/2000/svg">
    <rect class="card-face" x="0" y="0" width="910" height="525" rx="30" ry="30"/>
    <g class="brand-lockup">
      <circle class="brand-dot" cx="300" cy="250" r="84"/>
      <text class="brand-name" x="410" y="296">ZRT</text>
      <text class="brand-suffix" x="690" y="336" text-anchor="end">Pty Ltd</text>
    </g>
    <text class="web-address" x="455" y="462" text-anchor="middle">www.<tspan class="accent">zrtsupply</tspan>.com</text>
  </svg>

  <!-- Front of card -->
  <svg class="card card-front" viewBox="0 0 910 525" xmlns="http://www.w3.org/2000/svg">
    <defs>
      <clipPath id="card-shape">
        <rect x="0" y="0" width="910" height="525" rx="30" ry="30"/>
      </clipPath>
      <radialGradient id="photo-tones" cx="0.55" cy="0.72" r="0.75">
        <stop offset="0" stop-color="var(--photo-light)" stop-opacity="1"/>
        <stop offset="0.45" stop-color="var(--photo-mid)" stop-opacity="0.85"/>
        <stop offset="0.85" stop-color="#ffffff" stop-opacity="0"/>
      </radialGradient>
    </defs>
    <rect class="card-face" x="0" y="0" width="910" height="525" rx="30" ry="30"/>

    <g clip-path="url(#card-shape)">
      <rect class="product-photo" role="img" aria-label="Photo of a smiling baby"
            x="560" y="100" width="380" height="460" fill="url(#photo-tones)"/>
    </g>

    <g class="brand-lockup">
      <circle class="brand-dot" cx="134" cy="126" r="84"/>
      <text class="brand-name" x="246" y="170">ZRT</text>
      <text class="brand-suffix" x="533" y="206" text-anchor="end">Pty Ltd</text>
    </g>

    <g class="contact-block">
      <text class="person-name" x="45" y="303">Alex Marlow</text>
      <text class="person-role" x="45" y="330">Managing Director</text>
      <text class="contact-line" x="45" y="380">0000 Your Address Lakeview</text>
      <text class="contact-line" x="45" y="412">Texas 1234 USA</text>
      <text class="contact-line" x="45" y="452"><tspan class="contact-label">P:</tspan> 555 555 5555</text>
      <text class="contact-line" x="45" y="482"><tspan class="contact-label">E:</tspan> your@zrtsupply.com</text>
    </g>
  </svg>

</main>
</body>
</html>
```